Hualuoya herb bottle label

we need a new label design to reflect our branding for our Chinese herbal medicine product bottles. We import herbs from China and distribute them to Australian Practitioners. The product may be visible to their clients so we want to present it well. Our branding colours and images are attached below, as is the current label layout template. The manufacturer adds the individual names of the herbs and other details over the top so the back ground must be subtle. We would like our name - HuaLuoya at the top to possibly be in yellow/gold and in our chosen font (it will need to be saved and inserted as an image as last print run it reverted to a default font). we would like the blue mountains of the picture below incorporated as the back ground colours. The design needs to feel traditional and artistic. Our name Hualuoya means - essence and spirit. We represent the essence and spirit of traditional Chinese herbal medicine.

```html
<!DOCTYPE html>
<html lang="en">
<head>
<meta charset="UTF-8">
<title>Hualuoya Herb Bottle Label</title>
<link href="https://fonts.googleapis.com/css2?family=Arimo:wght@400;700&family=Cinzel:wght@500&family=Tinos&display=swap" rel="stylesheet">
<style>
  :root {
    --page: #eeeeee;
    --sky: #d6e6f3;
    --paper: #fbfbfb;
    --cream: #f3e8cc;
    --gold: #d8b45a;
    --seal-red: #e2483d;
    --band-red: #e8262c;
    --ink: #1d1d1d;
    --note-blue: #1f5d9c;
  }
  * { box-sizing: border-box; margin: 0; padding: 0; }
  html, body { width: 911px; height: 1200px; overflow: hidden; }
  body { background: var(--page); position: relative; font-family: "Arimo", Arial, sans-serif; color: var(--ink); }

  .label {
    position: absolute; left: 25px; top: 437px; width: 860px; height: 326px;
    background: linear-gradient(180deg, var(--sky) 0%, var(--paper) 28%, var(--paper) 80%, var(--cream) 100%);
    box-shadow: 0 6px 18px rgba(0,0,0,0.18);
    overflow: hidden;
  }
  .landscape {
    position: absolute; left: 0; top: 165px; width: 660px; height: 125px;
    background: linear-gradient(180deg, rgba(201,204,207,0) 0%, rgba(185,190,194,0.5) 45%, rgba(225,227,229,0.2) 100%);
  }
  .bamboo { position: absolute; top: 0; width: 120px; height: 100px; background: radial-gradient(ellipse at center, rgba(190,208,222,0.5), rgba(190,208,222,0) 70%); }
  .bamboo--left { left: 0; }
  .bamboo--right { right: 0; }

  .band { position: absolute; left: 0; width: 100%; height: 10px; background: var(--band-red); }
  .band--upper { top: 106px; }
  .band--lower { top: 128px; }

  .seal { position: absolute; background: var(--seal-red); border-radius: 2px; }
  .seal--left { left: 125px; top: 75px; width: 39px; height: 87px; }
  .seal--main { left: 383px; top: 76px; width: 53px; height: 122px; }
  .seal--right { left: 660px; top: 75px; width: 38px; height: 87px; }

  .brand { position: absolute; left: 248px; top: 16px; width: 320px; text-align: center; }
  .brand__name { font-family: "Cinzel", serif; font-weight: 500; font-size: 32px; color: var(--gold); letter-spacing: 1px; line-height: 36px; }
  .brand__tagline { font-family: "Tinos", serif; font-size: 14px; line-height: 16px; margin-top: 2px; }

  .product-type { position: absolute; left: 601px; top: 28px; font-size: 12px; line-height: 15px; }

  .supply { position: absolute; left: 601px; top: 191px; font-size: 9px; }
  .supply__note { color: var(--note-blue); font-size: 9.5px; line-height: 12px; margin-bottom: 10px; }
  .supply__address { line-height: 12.5px; }
  .supply__origin { font-weight: 700; font-size: 11px; margin-top: 9px; }

  .maker { position: absolute; left: 542px; top: 266px; width: 24px; height: 24px; border-radius: 50%; background: var(--seal-red); }

  .batch { position: absolute; left: 13px; top: 257px; width: 124px; height: 50px; background: #fff; font-size: 11.5px; padding: 5px 0 0 11px; line-height: 21px; }

  .net { position: absolute; left: 351px; top: 294px; width: 120px; text-align: center; font-weight: 700; font-size: 13px; line-height: 16px; }
</style>
</head>
<body>
  <div class="label">
    <div class="landscape" role="img" aria-label="Soft ink-wash misty mountain range with flying birds"></div>
    <div class="bamboo bamboo--left" role="img" aria-label="Faint bamboo leaves"></div>
    <div class="bamboo bamboo--right" role="img" aria-label="Faint bamboo leaves"></div>

    <div class="band band--upper"></div>
    <div class="band band--lower"></div>

    <div class="seal seal--left" role="img" aria-label="Red brand seal with Chinese characters"></div>
    <div class="seal seal--main" role="img" aria-label="Red brand seal with Chinese characters"></div>
    <div class="seal seal--right" role="img" aria-label="Red brand seal with Chinese characters"></div>

    <div class="brand">
      <div class="brand__name">HUALUOYA</div>
      <div class="brand__tagline">Concentrated Chinese Herbs</div>
    </div>

    <div class="product-type">Single Herb Granules<br>Concentrated Extract 5:1</div>

    <div class="supply">
      <p class="supply__note">Bulk for Practitioner Dispensing Only</p>
      <p class="supply__address">Tianhe Herbal Works Co. Ltd. China<br>Distributed by Hua Luoya Pty. Ltd.<br>212 Ridgeway Road<br>Kalamunda WA 6076<br>Australia</p>
      <p class="supply__origin">Product of China</p>
    </div>

    <div class="maker"></div>

    <div class="batch">BATCH NO:<br>USE BY:</div>

    <div class="net">100g NET</div>
  </div>
</body>
</html>
```